Copper Wren (short term rental)

This website will be for a short term rental (lodge h&h) located in a small quant town called Medicine Park and at the entrance of the Tallow Creek Reserve. I am currently in a logo contest and will have the logo soon to use on the website My goal for the website is to highlight the home and area with photographs, text, and possibly a rotating video/slide show of the local area. I will soon have a professional photographer at the home and will upload my own photos to the site with your instructions. I want a booking option for customers to use vs hosting sites like KELZ and lodge h&H. . I would like copperwren.org ( or .com—-appreciate your guidance here) for the web address. And I want it to appear on search engines with words like, medicine park, medicine park rental, rental near Wichita mountains, etc. I hope you can help me. Thanks!

Target Market(s)

Outdoor enthusiasts (bikers, hikers, lakers, etc) festival attendees, hippies.

Industry/Entity Type

Short term rental

Coding

Coded - Design and coding required

Number of Pages Required

1 page

Font styles to use
Serif

Colors
00AB8E
00BBA5
67D7C9
C6EFE9
E9F9F6

Requirements
Must have
• Booking calendar, reviews section, contact us section, brief over view of the area, place to upload my photos

```html
<!DOCTYPE html>
<html lang="en">
<head>
<meta charset="utf-8">
<title>Copper Wren – Medicine Park Vacation Home</title>
<link href="https://fonts.googleapis.com/css2?family=Lora:wght@400;600;700&display=swap" rel="stylesheet">
<style>
:root{
  --accent:#00BBA5;
  --accent-dark:#00AB8E;
  --accent-soft:#67D7C9;
  --accent-pale:#C6EFE9;
  --accent-mist:#E9F9F6;
  --ink:#222;
  --text:#444;
  --muted:#777;
  --line:#e3e3e3;
  --frame:#ededed;
  --foot:#f4f3f1;
}
*{box-sizing:border-box;margin:0;padding:0}
html,body{width:1200px;height:3690px;overflow:hidden}
body{background:var(--frame);font-family:'Lora',Georgia,serif;color:var(--text);position:relative}
a{color:inherit}
.page{position:absolute;left:26px;top:26px;width:1148px;height:3611px;background:#fff}

/* header */
.site-header{height:60px;display:flex;align-items:center;padding:0 32px}
.brand{font-weight:700;font-size:18px;line-height:19px;letter-spacing:1px;color:var(--accent-dark);width:130px}
.main-nav{display:flex;gap:24px;margin-left:28px;font-size:11px;font-weight:600;color:#333;text-transform:uppercase}
.dd::after{content:"";display:inline-block;width:5px;height:5px;border-right:1.5px solid #333;border-bottom:1.5px solid #333;transform:rotate(45deg);margin:0 0 2px 6px}
.header-tools{margin-left:auto;display:flex;align-items:center;gap:18px;font-size:11px;font-weight:600;color:#333;text-transform:uppercase}
.dot{width:10px;height:10px;border-radius:50%;background:#444;display:inline-block}
.flag{display:inline-block;width:14px;height:9px;background:#c33;margin-right:4px;vertical-align:-1px}
.tools-sep{width:1px;height:24px;background:var(--line)}

/* hero */
.hero{position:relative;height:544px;background:linear-gradient(180deg,#3c4a66 0%,#6b7590 35%,#c9b8a8 55%,#4a4e58 78%,#2b2f38 100%)}
.hero-copy{position:absolute;left:35px;top:199px;color:#fff;width:540px}
.tag{display:inline-block;background:#222;color:#fff;font-size:10px;padding:4px 8px}
.hero h1{font-size:26px;font-weight:700;margin:20px 0 26px}
.hero p{font-size:12.5px;line-height:20px}
.hero .lead-price{margin-top:22px}
.hero .lead-price u{text-decoration:underline dotted}
.btn{display:inline-block;background:var(--accent);color:#fff;font-size:11px;font-weight:700;text-transform:uppercase;text-align:center}
.hero .btn{margin-top:22px;width:87px;line-height:42px}
.slides{position:absolute;left:35px;top:490px;color:#fff;font-size:13px;font-weight:700;display:flex;align-items:center;gap:12px}
.slides i{width:26px;height:1.5px;background:#fff;display:inline-block;margin-right:4px}

/* intro / booking */
.intro{text-align:center;padding-top:66px}
.intro h2{font-size:27px;font-weight:400;color:var(--ink)}
.intro p{width:740px;margin:40px auto 0;font-size:12.5px;line-height:20px}
.search{display:flex;justify-content:center;gap:17px;margin-top:64px;text-align:left}
.field label{display:block;font-size:12.5px;color:var(--muted);margin-bottom:10px}
.field .box{height:44px;border:1px solid #ddd;display:flex;align-items:center;justify-content:space-between;padding:0 16px 0 18px;font-size:12.5px;color:#555}
.search-btn{display:block;margin:14px auto 0;width:98px;line-height:43px}

/* listings */
.listings{display:grid;grid-template-columns:repeat(3,358px);padding:0 35px;margin-top:70px;row-gap:52px}
.card-media{height:270px;position:relative}
.card-media .tag{position:absolute;left:27px;bottom:20px}
.card-body{padding:0 27px}
.card-body h3{font-size:18.5px;font-weight:600;color:var(--ink);margin-top:24px;line-height:27px}
.card-body .desc{font-size:12.5px;line-height:19.5px;margin-top:16px}
.stats{border-top:1px solid var(--line);border-bottom:1px solid var(--line);margin-top:22px;height:48px;display:flex;align-items:center;font-size:12.5px}
.stats span{display:flex;align-items:center;gap:12px;width:100px}
.stats svg{width:12px;height:12px;fill:#666}
.amen{font-size:10px;line-height:16px;color:#666;margin-top:16px}
.price{font-size:12.5px;line-height:19.5px;margin-top:16px}
.price b{margin-left:10px}
.price u{text-decoration:underline dotted;color:#666}
.actions{display:flex;align-items:center;gap:30px;margin-top:25px}
.actions .btn{width:87px;line-height:43px}
.actions a{font-size:11.5px;text-decoration:underline}

/* reviews */
.reviews{margin-top:142px;text-align:center}
.reviews h2{font-size:26px;font-weight:400;color:var(--ink)}
.review-row{display:grid;grid-template-columns:repeat(3,372px);padding:0 35px;margin-top:70px;text-align:left}
.review{display:flex;gap:26px}
.avatar{flex:none;width:88px;height:88px;border-radius:50%;background:linear-gradient(160deg,var(--accent-pale),#9aa8a6)}
.quote{font-size:12.5px;line-height:19.5px;width:210px}
.quote::before{content:"\201C";display:block;font-size:34px;color:#ccc;height:22px}
.quote cite{display:block;margin-top:12px;font-size:9.5px;font-style:normal;color:var(--accent)}
.quote cite a{text-decoration:underline}

/* footer */
.site-footer{position:absolute;left:0;top:3071px;width:1148px;height:451px;background:var(--foot);border-top:1px solid var(--line);display:grid;grid-template-columns:353px 353px 300px;padding:70px 0 0 79px}
.site-footer h4{font-size:11px;font-weight:700;color:#333;margin-bottom:28px}
.site-footer p{font-size:11px;line-height:16px;width:285px}
.site-footer .small{font-size:9.5px;line-height:16px;color:#666}
.site-footer ul{list-style:none;font-size:11px;line-height:16px}
.site-footer li{margin-bottom:19px;text-decoration:underline}
.bottom-bar{position:absolute;left:0;top:3522px;width:1148px;height:89px;border-top:1px solid var(--line);display:flex;align-items:center;justify-content:space-between;padding:0 0 0 79px;font-size:10.5px}
.bottom-bar .contact{margin-right:40px}
.chat{position:absolute;right:-22px;bottom:-14px;width:210px;height:48px;background:#fff;box-shadow:0 0 10px rgba(0,0,0,.2);display:flex;align-items:center;justify-content:space-between;padding:0 14px;font-size:11.5px;font-weight:700;color:#111}
.chat svg{width:16px;height:16px}
</style>
</head>
<body>
<div class="page">
  <header class="site-header">
    <div class="brand">COPPER<br>WREN</div>
    <nav class="main-nav">
      <span class="dd">The Home</span><span>Booking</span><span class="dd">The Area</span><span>Reviews</span><span class="dd">Photos</span><span>Contact</span>
    </nav>
    <div class="header-tools">
      <span class="dot"></span><span class="dot"></span><span class="dot"></span><span class="dot"></span>
      <span class="dd"><i class="flag"></i>English</span><span class="dd">USD</span>
      <span class="tools-sep"></span>
      <svg width="13" height="13" viewBox="0 0 13 13"><circle cx="5.5" cy="5.5" r="4" fill="none" stroke="#333" stroke-width="1.8"/><path d="M8.5 8.5l3.5 3.5" stroke="#333" stroke-width="1.8"/></svg>
    </div>
  </header>

  <section class="hero" role="img" aria-label="Photo slideshow of the Copper Wren house and Medicine Park at dusk">
    <div class="hero-copy">
      <span class="tag">Medicine Park</span>
      <h1>Copper Wren House</h1>
      <p>A cozy creekside home at the entrance of Tallow Creek Reserve, made for hikers, bikers, lakers and festival weekends.</p>
      <p class="lead-price">Prices start at: <b>$390</b> <u>for 3 nights</u> (+taxes and fees)</p>
      <span class="btn">Book</span>
    </div>
    <div class="slides">01 <i></i> 02 <span>03</span></div>
  </section>

  <section class="intro">
    <h2>Your basecamp in Medicine Park</h2>
    <p>Copper Wren sits in a quaint cobblestone town beside Tallow Creek Reserve. Book direct with us online quickly and safely, no booking fees.</p>
    <form class="search">
      <div class="field"><label>Check-in *</label><div class="box" style="width:214px">Check-in Date <svg width="12" height="12" viewBox="0 0 12 12"><rect x="1" y="2" width="10" height="9" fill="none" stroke="#444" stroke-width="1.3"/><path d="M1 5h10" stroke="#444"/></svg></div></div>
      <div class="field"><label>Check-out *</label><div class="box" style="width:214px">Check-out Date <svg width="12" height="12" viewBox="0 0 12 12"><rect x="1" y="2" width="10" height="9" fill="none" stroke="#444" stroke-width="1.3"/><path d="M1 5h10" stroke="#444"/></svg></div></div>
      <div class="field"><label>Adults</label><div class="box" style="width:90px">1 <svg width="9" height="6" viewBox="0 0 9 6"><path d="M1 1l3.5 3.5L8 1" fill="none" stroke="#444" stroke-width="1.3"/></svg></div></div>
      <div class="field"><label>Children</label><div class="box" style="width:90px">0 <svg width="9" height="6" viewBox="0 0 9 6"><path d="M1 1l3.5 3.5L8 1" fill="none" stroke="#444" stroke-width="1.3"/></svg></div></div>
    </form>
    <span class="btn search-btn">Search</span>
  </section>

  <svg width="0" height="0" style="position:absolute">
    <symbol id="i-guest" viewBox="0 0 12 12"><circle cx="6" cy="3.5" r="3"/><path d="M0 12c0-4 3-5.5 6-5.5s6 1.5 6 5.5z"/></symbol>
    <symbol id="i-bed" viewBox="0 0 12 12"><path d="M5 0h2v5h3l-4 3-4-3h3zM5 8h2v4H5z"/></symbol>
    <symbol id="i-area" viewBox="0 0 12 12"><path d="M0 0h4L0 4zM12 0v4L8 0zM0 12V8l4 4zM12 12H8l4-4zM3 3l6 6M9 3L3 9" stroke="#666" stroke-width="1.4"/></symbol>
    <symbol id="i-pin" viewBox="0 0 12 12"><path d="M6 0a4 4 0 0 1 4 4c0 3-4 8-4 8S2 7 2 4a4 4 0 0 1 4-4zm0 2.5a1.5 1.5 0 1 0 0 3 1.5 1.5 0 0 0 0-3z"/></symbol>
  </svg>

  <section class="listings">
    <article class="card">
      <div class="card-media" role="img" aria-label="Your photo: the whole house from the street" style="background:linear-gradient(180deg,#2e4a6e,#8a8f98 55%,#2a8fb0)"><span class="tag">The Home</span></div>
      <div class="card-body">
        <h3>The Whole House</h3>
        <p class="desc">Copper Wren is a fully equipped home with 3 bedrooms, a stone patio, fire pit and a short walk to the creek.</p>
        <div class="stats"><span><svg><use href="#i-guest"/></svg>8</span><span><svg><use href="#i-bed"/></svg>3</span><span><svg><use href="#i-area"/></svg>160m²</span></div>
        <p class="amen">Amenities: Air conditioning, Porch, Fire pit, Dining area, Flat-screen TV, Free parking, Free WiFi, Bike rack &nbsp;/ View: Creek &nbsp;/ Bed Type: 1 Queen bed, 2 Full beds, 2 Twin beds &nbsp;/ Categories: The Home</p>
        <p class="price">Prices start at: <b>$390</b> <u>for 3 nights</u> (+taxes and fees)</p>
        <div class="actions"><span class="btn">Book</span><a>View Details</a></div>
      </div>
    </article>
    <article class="card">
      <div class="card-media" role="img" aria-label="Your photo: the living room and kitchen" style="background:linear-gradient(180deg,#7a6a5a,#c8b8a4 50%,#e9f9f6)"><span class="tag">The Home</span></div>
      <div class="card-body">
        <h3>Living Room &amp; Kitchen</h3>
        <p class="desc">An open living space with a full kitchen, long dining table and big windows facing the granite hills of the reserve.</p>
        <div class="stats"><span><svg><use href="#i-guest"/></svg>8</span><span><svg><use href="#i-area"/></svg>60m²</span></div>
        <p class="amen">Amenities: Full kitchen, Coffee bar, Dining area, Flat-screen TV, Board games, Free WiFi, Washer &nbsp;/ View: Hills, Garden &nbsp;/ Seating: 1 Sofa bed, 8 Dining chairs &nbsp;/ Categories: The Home</p>
        <p class="price">Included with: <b>$390</b> <u>for 3 nights</u> (+taxes and fees)</p>
        <div class="actions"><span class="btn">Book</span><a>View Photos</a></div>
      </div>
    </article>
    <article class="card">
      <div class="card-media" role="img" aria-label="Your photo: the back deck and yard at sunset" style="background:linear-gradient(180deg,#3f8fd0,#e8ecef 45%,#67d7c9 80%,#c9a27a)"><span class="tag">The Home</span></div>
      <div class="card-body">
        <h3>Creekside Deck &amp; Yard</h3>
        <p class="desc">A shaded deck with string lights, a hammock and a grill, the perfect spot to rest after a day on the trails.</p>
        <div class="stats"><span><svg><use href="#i-guest"/></svg>10</span><span><svg><use href="#i-bed"/></svg>1</span><span><svg><use href="#i-area"/></svg>90m²</span></div>
        <p class="amen">Amenities: Grill, Hammock, Fire pit, Outdoor dining, String lights, Free parking, Pet friendly, Bike storage &nbsp;/ View: Creek &nbsp;/ Extras: 1 Daybed, 6 Camp chairs, 2 Kayaks &nbsp;/ Categories: The Home</p>
        <p class="price">Included with: <b>$390</b> <u>for 3 nights</u> (+taxes and fees)</p>
        <div class="actions"><span class="btn">Book</span><a>View Photos</a></div>
      </div>
    </article>
    <article class="card">
      <div class="card-media" role="img" aria-label="Photo of granite hills and trails in Tallow Creek Reserve" style="background:linear-gradient(180deg,#8d8f94,#d7b58c 45%,#b98a5c 75%,#7a5a40)"><span class="tag">The Area</span></div>
      <div class="card-body">
        <h3>Tallow Creek Reserve</h3>
        <p class="desc">Hike granite peaks, spot bison and longhorns, and climb boulders right at the entrance, minutes from the door.</p>
        <div class="stats"><span><svg><use href="#i-pin"/></svg>1 mi</span><span><svg><use href="#i-area"/></svg>240km²</span></div>
        <p class="amen">Activities: Hiking, Rock climbing, Mountain biking, Wildlife viewing, Picnics, Camping, Stargazing &nbsp;/ Trails: 15 marked routes &nbsp;/ Best time: Spring and Fall &nbsp;/ Categories: The Area</p>
        <p class="price">Distance: <b>2 min</b> <u>by car</u> (or 20 min walk)</p>
        <div class="actions"><span class="btn">Book</span><a>Area Guide</a></div>
      </div>
    </article>
    <article class="card">
      <div class="card-media" role="img" aria-label="Photo of the cobblestone main street of Medicine Park" style="background:linear-gradient(180deg,#3e86d6,#9a7a5c 40%,#c6efe9 70%,#e9f9f6)"><span class="tag">The Area</span></div>
      <div class="card-body">
        <h3>Cobblestone Town of Medicine Park</h3>
        <p class="desc">Stroll the cobblestone streets, local shops, cafés and live music, with festivals and art fairs all year round.</p>
        <div class="stats"><span><svg><use href="#i-pin"/></svg>0.3 mi</span><span><svg><use href="#i-guest"/></svg>Walk</span><span><svg><use href="#i-area"/></svg>Town</span></div>
        <p class="amen">Highlights: Cobblestone cottages, Swim beach, Cafés, Galleries, Live music, Festivals, Farmers market &nbsp;/ Events: Spring, Summer, Fall &nbsp;/ Walk: 6 minutes &nbsp;/ Categories: The Area</p>
        <p class="price">Distance: <b>6 min</b> <u>on foot</u> (along the creek)</p>
        <div class="actions"><span class="btn">Book</span><a>Area Guide</a></div>
      </div>
    </article>
    <article class="card">
      <div class="card-media" role="img" aria-label="Photo of the nearby lake with kayaks" style="background:linear-gradient(180deg,#5f95d8,#dfe6ec 45%,#67d7c9 75%,#00bba5)"><span class="tag">The Area</span></div>
      <div class="card-body">
        <h3>Lakes &amp; Swimming Holes</h3>
        <p class="desc">Paddle, fish and swim at the nearby lakes and clear creek pools, perfect for lakers and summer families.</p>
        <div class="stats"><span><svg><use href="#i-pin"/></svg>4 mi</span><span><svg><use href="#i-area"/></svg>3 lakes</span></div>
        <p class="amen">Activities: Kayaking, Paddle boarding, Fishing, Swimming, Boat ramps, Picnic areas, Sunset views, Cliff overlooks &nbsp;/ Gear: 2 Kayaks at the house &nbsp;/ Categories: The Area</p>
        <p class="price">Distance: <b>8 min</b> <u>by car</u> (free parking)</p>
        <div class="actions"><span class="btn">Book</span><a>Area Guide</a></div>
      </div>
    </article>
  </section>

  <section class="reviews">
    <h2>Guest Reviews</h2>
    <div class="review-row">
      <div class="review"><div class="avatar" role="img" aria-label="Guest portrait"></div><blockquote class="quote">We came for the hiking and stayed by chance at Copper Wren. Trailheads minutes away and a cozy house to come back to!<cite>— <a>SAM ARCHER</a></cite></blockquote></div>
      <div class="review"><div class="avatar" role="img" aria-label="Guest portrait"></div><blockquote class="quote">I'll never forget our festival weekend at Copper Wren! Perfect location, easy booking, amazing creek views. We walked to town every night and would recommend it to everyone. There are so many things to do – music, art fairs, lakes, trails and much more!<cite>— <a>LIA MORENO</a></cite></blockquote></div>
      <div class="review"><div class="avatar" role="img" aria-label="Guest portrait"></div><blockquote class="quote">I was visiting Medicine Park with my family and friends and stayed at Copper Wren – an amazing stay! A lot of space, a fire pit, the creek, just a peaceful rest.<cite>— <a>BEN CALDER</a></cite></blockquote></div>
    </div>
  </section>

  <footer class="site-footer">
    <div>
      <h4>ABOUT US</h4>
      <p>Copper Wren is a locally owned vacation home in Medicine Park, at the entrance of Tallow Creek Reserve. Book direct with us for the best rates and a warm welcome.</p>
      <h4 style="margin-top:38px">THE AREA</h4>
      <p class="small">Medicine Park is a small cobblestone resort town with creeks, swim beaches, galleries and live music. It's an easy drive to trails, lakes and climbing spots (hiking maps are waiting for you at the house).</p>
      <p class="small" style="margin-top:22px">Note: check-in is 4 pm, check-out is 11 am. Pets are welcome on request.</p>
    </div>
    <div>
      <h4>LOCAL GUIDE</h4>
      <ul><li>Best hiking trails in Tallow Creek Reserve</li><li>Spring festivals and live music in town</li><li>Where to swim, paddle and fish nearby</li><li>Biking routes for every level of rider</li><li>Cafés and shops on the cobblestone street?</li></ul>
    </div>
    <div>
      <h4>CONTACT US</h4>
      <ul><li>hello@copperwren.org</li><li>+1 (580) 555-0142</li><li>12 Creek Rd, Medicine Park</li><li>How to book</li><li>House rules</li></ul>
    </div>
  </footer>
  <div class="bottom-bar"><span>© 2022 Copper Wren</span><span class="contact">+1 (580) 555-0142 &nbsp;/&nbsp; 12 Creek Rd, Medicine Park</span>
    <div class="chat">We are Online! <svg viewBox="0 0 16 16"><path d="M2 2h12v9H6l-4 3z" fill="none" stroke="#1a73e8" stroke-width="1.8"/></svg></div>
  </div>
</div>
</body>
</html>
```